High End Business Card Design for Flooring Store

Looking for a new card design for our hardwood flooring company. We have no print budget for these and are open to cards made from wood, metal, cardstock with embossed print ... or any combination of these. No plastic.

We sell luxury products and I want the cards to reflect our image of quality and class.

Our contact information as such;
Employee Name
418 Colbrook Blvd.
Dieppe, NB
K9R-3M5
(555) 214-3968
Employee email @velkaflooring.com

Target Market(s)

Home Builders

Contact Information for Business Card

Emnployee name, business contact information

```html
<!DOCTYPE html>
<html lang="en">
<head>
<meta charset="utf-8">
<title>Velka Flooring – Business Card</title>
<link rel="stylesheet" href="https://fonts.googleapis.com/css2?family=Montserrat:wght@600&family=Quicksand:wght@500&display=swap">
<style>
  :root {
    --stage: #d9d9d9;
    --card-dark: #2f2f31;
    --wood-dark: #26272a;
    --wood-mid: #3b3c40;
    --accent-red: #a8302f;
    --gold: #e3aa2b;
    --text-light: #ececec;
    --text-soft: #c9c9c9;
  }
  * { box-sizing: border-box; margin: 0; padding: 0; }
  html, body { width: 1200px; height: 1200px; overflow: hidden; }
  body {
    background: var(--stage);
    display: flex;
    flex-direction: column;
    align-items: center;
    justify-content: space-evenly;
    font-family: "Quicksand", sans-serif;
  }
  .card {
    position: relative;
    width: 900px;
    height: 514px;
    border-radius: 6px;
    overflow: hidden;
    box-shadow: 0 10px 30px rgba(0,0,0,.25);
  }

  /* Front */
  .card--front { background: var(--wood-dark); }
  .card__wood {
    position: absolute; inset: 0;
    background: radial-gradient(ellipse at 35% 40%, var(--wood-mid) 0%, var(--wood-dark) 75%);
  }
  .front__brand {
    position: absolute; inset: 0;
    display: flex; align-items: center; justify-content: center;
  }
  .company-name {
    font-family: "Quicksand", sans-serif;
    font-weight: 500;
    color: var(--text-light);
    line-height: 1;
  }
  .front__brand .company-name { font-size: 64px; letter-spacing: 2px; }

  /* Back */
  .card--back { background: var(--card-dark); }
  .back__brand { position: absolute; top: 80px; right: 70px; }
  .back__brand .company-name { font-size: 30px; }

  .employee { position: absolute; left: 70px; top: 130px; }
  .employee__name {
    font-family: "Montserrat", sans-serif;
    font-weight: 600;
    font-size: 42px;
    letter-spacing: 1px;
    color: var(--gold);
    line-height: 1.1;
  }
  .employee__role {
    font-size: 22px;
    font-weight: 500;
    color: var(--text-soft);
    margin-top: 4px;
  }

  .contact { position: absolute; left: 70px; top: 265px; list-style: none; }
  .contact__item {
    display: flex; align-items: center; gap: 22px;
    height: 50px;
    color: var(--text-light);
    font-size: 21px;
    font-weight: 500;
  }
  .contact__icon { width: 26px; height: 26px; flex: none; fill: var(--accent-red); }
  .contact__icon--stroke { fill: none; stroke: var(--accent-red); stroke-width: 2.2; }
</style>
</head>
<body>

  <section class="card card--front" aria-label="Card front">
    <div class="card__wood" role="img" aria-label="Dark charcoal wood grain texture"></div>
    <div class="front__brand">
      <div class="company-name">Velka</div>
    </div>
  </section>

  <section class="card card--back" aria-label="Card back">
    <div class="back__brand">
      <div class="company-name">Velka</div>
    </div>

    <div class="employee">
      <h1 class="employee__name">EMPLOYEE NAME</h1>
      <p class="employee__role">Position</p>
    </div>

    <ul class="contact">
      <li class="contact__item">
        <svg class="contact__icon" viewBox="0 0 24 24" aria-hidden="true"><path d="M12 2a7 7 0 0 0-7 7c0 5.2 7 13 7 13s7-7.8 7-13a7 7 0 0 0-7-7zm0 9.5A2.5 2.5 0 1 1 12 6.5a2.5 2.5 0 0 1 0 5z"/></svg>
        <span>418 Colbrook Blvd. Dieppe, NB K9R-3M5</span>
      </li>
      <li class="contact__item">
        <svg class="contact__icon" viewBox="0 0 24 24" aria-hidden="true"><path d="M6.6 10.8a15.1 15.1 0 0 0 6.6 6.6l2.2-2.2a1 1 0 0 1 1-.25 11.4 11.4 0 0 0 3.6.57 1 1 0 0 1 1 1V20a1 1 0 0 1-1 1A17 17 0 0 1 3 4a1 1 0 0 1 1-1h3.5a1 1 0 0 1 1 1 11.4 11.4 0 0 0 .57 3.6 1 1 0 0 1-.25 1z"/></svg>
        <span>(555) 214-3968</span>
      </li>
      <li class="contact__item">
        <svg class="contact__icon" viewBox="0 0 24 24" aria-hidden="true"><path d="M2 5h20v14H2z"/><path d="M2 6.5l10 8 10-8V5H2z" fill="#2f2f31"/></svg>
        <span>Employee email @velkaflooring.com</span>
      </li>
      <li class="contact__item">
        <svg class="contact__icon contact__icon--stroke" viewBox="0 0 24 24" aria-hidden="true"><circle cx="12" cy="12" r="9.5"/><path d="M2.5 12h19M12 2.5c3 3 3 16 0 19M12 2.5c-3 3-3 16 0 19"/></svg>
        <span>www.velkaflooring.com</span>
      </li>
    </ul>
  </section>

</body>
</html>
```